Infografik für Tanzschule
Zielgruppe
Wir sind eine Tanzschule für die Tänze Salsa, Bachata, kizomba & Zouk in Freiburg
Aufgabenstellung
DESIGN-BRIEFING
Tarifübersicht – Tanzschule Ritmo del Alba
Projektziel
Gestaltung einer klaren, hochwertigen Tarifübersicht für eine Tanzschule.
Die Grafik dient: als Information & Orientierung auf der Homepage, als visuelle Grundlage für das Anmeldeformular vor Ort, Der Einstieg erfolgt immer über eine gratis Schnupperstunde.
Die verbindliche Anmeldung erfolgt nach der Schnupperstunde vor Ort über ein Formular mit Auswahlkästchen.
Grundaufbau
3 Tarifkarten nebeneinander
Einheitlicher, moderner Stil
evtl. Emotionale Bilder (echte Tanzszenen, echte Menschen)
Klare Hierarchie:
Titel → Preis → Erklärung → Vorteile → Auswahlkästchen
Struktur der Tarifkarten
KARTE 1 – EINSTIEG
Titel: 1× PRO WOCHE TANZEN
Preis: 56 €/ 39 € erm.
Subline: pro Person · pro Kalendermonat
Vorteile (max. 4 Bulletpoints):
Ein fester wöchentlicher Kurs
Klare Routine & Struktur
Ausweichstunde im selben Monat möglich (muss klar enthalten sein)
Auswahl: ☐ 1× pro Woche tanzen
KARTE 2 – REGELMÄSSIG TANZEN (darf visuell leicht hervorgehoben sein, z. B. Rahmen oder Badge)
Optionales Badge:
SEHR BELIEBT
Titel: 2× PRO WOCHE TANZEN
Preis: 98 € / 68 € erm.
Vorteile:
Zwei feste wöchentliche Kurse
Mehr Praxis & schnellerer Fortschritt
Ausweichstunde im selben Monat möglich
Auswahl:
☐ 2× pro Woche tanzen
KARTE 3 – MAXIMALE FREIHEIT
Titel: FLAT – ALL YOU CAN DANCE
Preis: ab 129 € / 99 € erm.
Alle Tänze
Alle Kurse (für dein Tanz-Level)
Alle Workshops (für dein Tanz-Level)
Maximale Freiheit
☐ FLAT 1 Monat – 149 € | 119 € erm. (monatlich kündbar)
☐ FLAT 3 Monate – 129 € | 99 € erm. (3 Monate Erstlaufzeit)
Einheitlicher Hinweis unter den Karten (kleiner Text)
Ausweic..

```html
<!DOCTYPE html>
<html lang="de">
<head>
<meta charset="utf-8">
<title>Anmeldeformular – Ritmo del Alba</title>
<link href="https://fonts.googleapis.com/css2?family=Inter:ital,wght@0,300;0,400;0,500;0,600;0,700;1,400&family=Roboto+Condensed:wght@400;500;700&display=swap" rel="stylesheet">
<style>
  :root{
    --backdrop:#9e9e9e;
    --paper:#ffffff;
    --ink:#2b2b2b;
    --muted:#555;
    --soft:#8a8a8a;
    --rule:#bdbdbd;
    --card-bg:#f3f3f3;
    --card-head:#6f6f6f;
    --card-head-dark:#2a2a2a;
    --mint:#dbe4df;
    --photo-a:#9a8a7c;
    --photo-b:#c9b9a6;
  }
  *{box-sizing:border-box;margin:0;padding:0}
  html,body{width:1200px;height:1200px;overflow:hidden;background:var(--backdrop)}
  body{font-family:"Inter",sans-serif;color:var(--ink);position:relative}
  .sheet{position:absolute;left:302px;top:179px;width:894px;height:1263px;background:var(--paper);transform:scale(.6667);transform-origin:0 0;overflow:hidden}
  .brand{position:absolute;left:40px;top:62px;width:230px;text-align:center}
  .brand-name{display:block;font-size:26px;font-weight:400;color:var(--ink);letter-spacing:.5px}
  .brand-tag{display:block;font-size:8px;color:var(--muted);margin-top:4px}
  .hero{position:absolute;left:315px;top:0;width:579px;height:204px;background:linear-gradient(100deg,var(--photo-a),var(--photo-b) 45%,#b08f72 70%,#c96b5e)}
  .hero-split{position:absolute;top:0;height:204px;width:6px;background:#fff;opacity:.8;transform:skewX(-20deg)}
  .form-title{position:absolute;left:44px;top:161px;width:274px;height:43px;background:var(--card-head-dark);color:#fff;font-size:23px;font-weight:700;letter-spacing:-.5px;padding:7px 16px}
  .box{display:inline-block;width:11px;height:11px;border:1.3px solid var(--ink);border-radius:2px;vertical-align:-1px}
  .salutation{position:absolute;left:44px;top:228px;font-size:12px;color:var(--muted)}
  .salutation .box{margin:0 4px 0 4px}
  .field{position:absolute;left:44px;width:560px;height:20px;font-size:13.5px;color:var(--muted)}
  .field .colon{position:absolute;left:143px}
  .field .line{position:absolute;left:152px;right:0;bottom:-2px;border-bottom:1px solid var(--rule)}
  .option{position:absolute;left:44px;font-size:13.5px;color:var(--muted)}
  .option .box{margin-right:8px}
  .contact{position:absolute;left:654px;top:230px;width:192px;height:219px;background:var(--card-bg);border:1px solid #e0e0e0;border-radius:7px;padding:18px 8px;font-size:11.5px;color:var(--muted);line-height:17px}
  .contact strong{color:var(--ink);font-weight:600}
  .contact p{margin-bottom:17px}
  .contact .k{color:var(--ink);font-weight:600}
  .card{position:absolute;top:473px;width:255px;height:397px;background:var(--card-bg);border:1px solid #d6d6d6;border-radius:5px;overflow:hidden}
  .card-head{height:141px;background:var(--card-head);color:#fff;padding:15px 15px 0}
  .card--featured .card-head{background:var(--card-head-dark)}
  .card-title{font-size:28px;font-weight:300;line-height:29px;letter-spacing:-.5px}
  .price{margin-top:16px;border-left:4px solid #d8d8d8;padding-left:9px;line-height:18px}
  .price b{font-size:20px;font-weight:400}
  .price small{font-size:13px}
  .price span{display:block;font-size:12px;color:#d0d0d0}
  .badge{position:absolute;right:0;top:0;background:#d9d9d9;color:var(--ink);font-size:11.5px;padding:3px 6px;border-radius:0 0 0 6px}
  .card-body{padding:16px 14px 0}
  .perks-title{font-size:15px;font-weight:600;padding-bottom:4px;border-bottom:2px solid var(--ink);letter-spacing:.3px}
  .perks{list-style:none;font-size:12.5px;color:var(--muted)}
  .perks li{padding:8px 0 4px;border-bottom:1px solid #ddd;line-height:15px}
  .choice{font-size:12.5px;color:var(--ink);margin-top:22px}
  .choice .box{margin-right:7px}
  .choice em{display:block;font-size:12px;color:var(--muted);margin-top:4px}
  .card--flat .choice{margin-top:14px}
  .card--flat .choice + .choice{margin-top:8px}
  .note{position:absolute;top:895px;font-size:13.5px}
  .note h3{font-size:13.5px;font-weight:600;margin-bottom:4px}
  .note p{border-left:3px solid #cfcfcf;padding-left:11px;font-style:italic;color:var(--muted);font-size:12.5px;line-height:19px}
  .band{position:absolute;left:0;top:983px;width:894px;height:280px;background:var(--mint);font-family:"Roboto Condensed",sans-serif}
  .sepa{position:absolute;left:70px;top:19px;width:798px;height:153px;background:#fff;padding:10px 14px}
  .sepa h4{font-size:11.5px;font-weight:700}
  .sepa p{font-size:9.4px;line-height:13.5px;color:var(--muted)}
  .bank{margin-top:4px;border:1.5px solid var(--ink)}
  .bank-row{display:flex;height:36px;font-size:10.5px}
  .bank-row+.bank-row{border-top:1.5px solid var(--ink)}
  .bank-cell{padding:4px 8px}
  .bank-cell+.bank-cell{border-left:1.5px solid var(--ink)}
  .iban{display:flex;align-items:flex-end;height:100%;padding-bottom:0}
  .iban-label{padding:4px 8px;width:40px}
  .iban-cells{display:flex;align-items:flex-end;margin-left:0}
  .iban-cells i{display:block;width:15.5px;height:16px;border-left:1.3px solid var(--ink);font-style:normal;font-size:19px;font-weight:500;text-align:center;line-height:16px;margin-bottom:4px}
  .iban-cells i.grp{height:22px}
  .months{position:absolute;left:70px;top:192px;width:321px;height:38px;background:#fff;display:flex;justify-content:space-around;padding:6px 4px 0;font-size:9.5px;text-align:center}
  .months span{display:flex;flex-direction:column;align-items:center;gap:2px}
  .sign{position:absolute;left:495px;top:192px;width:373px;height:49px;background:#fff}
  .label{position:absolute;font-size:18px;font-weight:500;color:var(--ink)}
  .label small{font-size:9.5px;font-weight:500;margin-left:4px}
</style>
</head>
<body>
<div class="sheet">
  <div class="brand">
    <span class="brand-name">Ritmo del Alba</span>
    <span class="brand-tag">Tanzschule im Herzen Freiburgs</span>
  </div>
  <div class="hero" role="img" aria-label="Fotostreifen mit tanzenden Menschen im Kurs">
    <span class="hero-split" style="left:140px"></span>
    <span class="hero-split" style="left:290px"></span>
    <span class="hero-split" style="left:450px"></span>
  </div>
  <div class="form-title">Anmeldeformular</div>

  <div class="salutation">Frau <span class="box"></span> Herr <span class="box"></span> Div. <span class="box"></span></div>
  <div class="field" style="top:253px">Vorname / Nachname<span class="colon">:</span><span class="line"></span></div>
  <div class="field" style="top:283px">Straße / Nr<span class="colon">:</span><span class="line"></span></div>
  <div class="field" style="top:313px">PLZ/Ort<span class="colon">:</span><span class="line"></span></div>
  <div class="field" style="top:343px">Telefon<span class="colon">:</span><span class="line"></span></div>
  <div class="field" style="top:373px">E-mail<span class="colon">:</span><span class="line"></span></div>
  <div class="option" style="top:403px"><span class="box"></span>Ermäßigt (Student*in / Schüler*in / Auszubildende*r)</div>
  <div class="option" style="top:427px"><span class="box"></span>Ja, ich möchte den Newsletter und Kursinformationen erhalten.</div>

  <div class="contact">
    <p><strong>Tanzschule Ritmo del Alba</strong><br>Lindenweg 14 79098 Freiburg</p>
    <p><strong>Geschäftsanschrift</strong><br>Ritmo del Alba Lena Hartmann<br>Ahornstr. 8 79104 Freiburg</p>
    <div style="line-height:21px"><span class="k">T :</span> +49 152 000 418 66<br><span class="k">M :</span> info@ritmo-del-alba.de<br><span class="k">W :</span> www.ritmo-del-alba.de</div>
  </div>

  <div class="card" style="left:47px">
    <div class="card-head">
      <div class="card-title">1× Pro Woche<br>Tanzen</div>
      <div class="price"><b>€56</b> <small>/ 39 € erm.</small><span>pro Person / Kalendermonat</span></div>
    </div>
    <div class="card-body">
      <div class="perks-title">VORTEILE</div>
      <ul class="perks"><li>Ein fester wöchentlicher Kurs</li><li>Klare Routine &amp; Struktur</li><li>Ausweichstunde im selben Monat möglich</li></ul>
      <div class="choice"><span class="box"></span>1× pro Woche tanzen</div>
    </div>
  </div>

  <div class="card card--featured" style="left:318px">
    <span class="badge">Sehr Beliebt</span>
    <div class="card-head">
      <div class="card-title">Regelmässig<br>Tanzen</div>
      <div class="price"><b>€98</b> <small>/ 68 € erm.</small><span>pro Person / Kalendermonat</span></div>
    </div>
    <div class="card-body">
      <div class="perks-title">VORTEILE</div>
      <ul class="perks"><li>Zwei feste wöchentliche Kurse</li><li>Mehr Praxis &amp; schnellerer Fortschritt</li><li>Ausweichstunde im selben Monat möglich</li></ul>
      <div class="choice"><span class="box"></span>2× pro Woche tanzen</div>
    </div>
  </div>

  <div class="card card--flat" style="left:589px">
    <div class="card-head">
      <div class="card-title">Flat – All You Can<br>Dance</div>
      <div class="price"><b>ab129€</b> <small>/ 99 € erm.</small><span>pro Person / Kalendermonat</span></div>
    </div>
    <div class="card-body">
      <div class="perks-title">VORTEILE</div>
      <ul class="perks"><li>Alle Tänze</li><li>Alle Kurse (für dein Tanz-Level)</li><li>Alle Workshops (für dein Tanz-Level)</li><li>Maximale Freiheit</li></ul>
      <div class="choice"><span class="box"></span>FLAT 1 Monat – 149 € | 119 € erm.<em>(monatlich kündbar)</em></div>
      <div class="choice"><span class="box"></span>FLAT 3 Monate – 129 € | 99 € erm.<em>(3 Monate Erstlaufzeit)</em></div>
    </div>
  </div>

  <div class="note" style="left:70px;width:200px">
    <h3>Hinweis</h3>
    <p>Ausweichstunde: Im selben Kalendermonat möglich.</p>
  </div>
  <div class="note" style="left:339px;width:540px">
    <h3>Verlängerung &amp; Kündigung</h3>
    <p>Der Vertrag verlängert sich automatisch um jeweils einen Monat und ist mit 14 Tagen Frist zum Monatsende kündbar.<br>Ausnahme: FLAT 3 Monate – kündbar nach Ablauf der Erstlaufzeit.</p>
  </div>

  <div class="band">
    <div class="sepa">
      <h4>Einzugsermächtigung / SEPA-Lastschriftmandat</h4>
      <p>Ich ermächtige Ritmo del Alba, Zahlungen von meinem Konto per Lastschrift einzuziehen und mein Kreditinstitut, diese Lastschriften einzulösen. Bei Ablehnung der Lastschrift fallen Kosten von 10,00 € pro Rückbuchung an. Ich kann innerhalb von acht Wochen ab Belastungsdatum die Erstattung verlangen, gemäß den Bedingungen meines Kreditinstituts. Die Kursgebühr wird im ersten Monat zur Mitte/Ende eingezogen, danach jeweils am 05. jedes Monats.</p>
      <div class="bank">
        <div class="bank-row"><div class="bank-cell" style="width:444px">Kreditinstitut:</div><div class="bank-cell" style="flex:1">BIC: - Beginnt die IBAN mit DE, dann ist kein BIC nötig</div></div>
        <div class="bank-row">
          <div class="iban"><span class="iban-label" style="align-self:flex-start">IBAN:</span>
            <div class="iban-cells">
              <i>D</i><i>E</i><i class="grp"></i><i></i><i></i><i class="grp"></i><i></i><i></i><i></i><i class="grp"></i><i></i><i></i><i></i><i class="grp"></i><i></i><i></i><i></i><i class="grp"></i><i></i><i></i><i></i><i class="grp"></i><i></i><i></i><i></i><i class="grp"></i><i></i><i></i><i></i><i class="grp"></i><i></i><i></i><i></i><i class="grp"></i><i></i><i></i><i></i><i class="grp"></i><i></i><i></i><i></i><i class="grp"></i><i></i><i></i>
            </div>
          </div>
        </div>
      </div>
    </div>
    <div class="months">
      <span>Jan<i class="box"></i></span><span>Feb<i class="box"></i></span><span>Mrz<i class="box"></i></span><span>Apr<i class="box"></i></span><span>Mai<i class="box"></i></span><span>Jun<i class="box"></i></span><span>Jul<i class="box"></i></span><span>Aug<i class="box"></i></span><span>Sep<i class="box"></i></span><span>Okt<i class="box"></i></span><span>Nov<i class="box"></i></span><span>Dez<i class="box"></i></span>
    </div>
    <div class="label" style="left:72px;top:236px">Kursstart / Anmeldung ab:</div>
    <div class="sign"></div>
    <div class="label" style="left:495px;top:246px">Datum / Unterschrift:<small>Wir verweisen auf unsere umseitig abgedruckten AGB</small></div>
  </div>
</div>
</body>
</html>
```